pharmacy/travel clinic business card design

We need a business card for our new business called Brenwick Travel Clinic and Pharmacy. Our primary focus is doing consultations for people before travelling internationally and providing vaccinations and prescriptions for them. While the business is considered a pharmacy, it has more the look and feel of a doctor's office. The design should communicate a professional and trustworthy feel. I have attached a copy of the logo we are going to be using.
Updates
Thanks for the submissions.  If you haven`t been eliminated you are one of the finalists.  Decision will likely be made tomorrow.

Target Market(s)
Customers, other health care professionals, travel agents
Industry/Entity Type
Clinic
Look and feel
Each slider illustrates characteristics of the customer's brand and the style your logo design should communicate.

```html
<!DOCTYPE html>
<html lang="en">
<head>
<meta charset="utf-8">
<title>Brenwick Travel Clinic and Pharmacy – Business Card</title>
<link rel="stylesheet" href="https://fonts.googleapis.com/css2?family=Arimo:wght@400;700&display=swap">
<style>
  :root {
    --canvas-bg: #ecebe8;
    --green-deep: #0f8a0f;
    --green-bright: #33d017;
    --green-text: #7cbc3a;
    --ink: #1c1c1c;
    --muted: #555555;
    --card-white: #ffffff;
    --card-grey: #ececec;
  }
  html, body {
    margin: 0;
    padding: 0;
    overflow: hidden;
  }
  body {
    width: 1200px;
    height: 723px;
    background: var(--canvas-bg);
    font-family: "Arimo", Arial, sans-serif;
    position: relative;
  }
  .card {
    position: absolute;
    width: 525px;
    height: 300px;
    top: 211px;
    border-radius: 2px;
    box-shadow: 0 6px 18px rgba(0,0,0,0.18);
    overflow: hidden;
  }
  .card--front {
    left: 50px;
    background: radial-gradient(ellipse at 50% 50%, var(--green-bright) 0%, #1daa12 45%, var(--green-deep) 100%);
  }
  .card--back {
    left: 625px;
    background: linear-gradient(120deg, var(--card-grey) 0%, var(--card-white) 55%, #f4f4f4 100%);
  }
  .decor-circle {
    position: absolute;
    border-radius: 50%;
  }
  .card--front .decor-circle {
    width: 240px;
    height: 240px;
    right: 40px;
    top: -60px;
    background: rgba(255,255,255,0.08);
  }
  .card--back .decor-circle {
    width: 220px;
    height: 220px;
    right: 30px;
    top: -30px;
    background: rgba(0,0,0,0.035);
  }
  .wordmark {
    position: absolute;
    display: flex;
    align-items: center;
    gap: 10px;
  }
  .wordmark__dot {
    width: 14px;
    height: 14px;
    border-radius: 50%;
    flex: none;
  }
  .wordmark__name {
    font-weight: 700;
    font-size: 23px;
    line-height: 1.05;
    letter-spacing: -0.3px;
  }
  .card--front .wordmark {
    left: 120px;
    top: 178px;
  }
  .card--front .wordmark__dot { background: #ffffff; }
  .card--front .wordmark__name { color: #ffffff; }
  .card--back .wordmark {
    right: 44px;
    top: 48px;
  }
  .card--back .wordmark__dot { background: var(--green-text); }
  .card--back .wordmark__name { color: var(--green-text); }
  .person {
    position: absolute;
    left: 40px;
    top: 150px;
  }
  .person__name {
    margin: 0;
    font-weight: 700;
    font-size: 19px;
    color: var(--green-text);
    letter-spacing: 0.3px;
  }
  .person__role {
    margin: 3px 0 0;
    font-size: 10px;
    color: var(--muted);
    letter-spacing: 0.6px;
  }
  .contact {
    list-style: none;
    margin: 0;
    padding: 0;
    position: absolute;
    left: 40px;
    top: 202px;
  }
  .contact__item {
    display: flex;
    align-items: center;
    gap: 12px;
    font-size: 12px;
    color: var(--ink);
    height: 17px;
  }
  .contact__icon {
    width: 10px;
    height: 10px;
    flex: none;
    fill: var(--green-text);
  }
</style>
</head>
<body>
  <section class="card card--front" aria-label="Card front">
    <div class="decor-circle"></div>
    <div class="wordmark">
      <span class="wordmark__dot"></span>
      <span class="wordmark__name">Brenwick Travel Clinic<br>and Pharmacy</span>
    </div>
  </section>

  <section class="card card--back" aria-label="Card back">
    <div class="decor-circle"></div>
    <div class="wordmark">
      <span class="wordmark__dot"></span>
      <span class="wordmark__name">Brenwick Travel Clinic<br>and Pharmacy</span>
    </div>

    <div class="person">
      <h1 class="person__name">AARON WEXLEY</h1>
      <p class="person__role">PRESIDENT</p>
    </div>

    <ul class="contact">
      <li class="contact__item">
        <svg class="contact__icon" viewBox="0 0 10 10" aria-hidden="true"><path d="M5 0.5 L9.5 5 H8 V9.5 H6 V6.5 H4 V9.5 H2 V5 H0.5 Z"/></svg>
        Po Box 4815, U.K SE719
      </li>
      <li class="contact__item">
        <svg class="contact__icon" viewBox="0 0 10 10" aria-hidden="true"><path d="M2 0.5 L4 2.5 L3 4 Q4.5 6 6 7 L7.5 6 L9.5 8 L8 9.5 Q3 9 0.5 2 Z"/></svg>
        1300 482 916
      </li>
      <li class="contact__item">
        <svg class="contact__icon" viewBox="0 0 10 10" aria-hidden="true"><rect x="2.5" y="0.5" width="5" height="9" rx="1"/></svg>
        07 3958 2204
      </li>
      <li class="contact__item">
        <svg class="contact__icon" viewBox="0 0 10 10" aria-hidden="true"><path d="M0.5 2 H9.5 V8.5 H0.5 Z M0.5 2 L5 5.5 L9.5 2" stroke="#fff" stroke-width="0.8"/></svg>
        hello@brenwickclinic.com
      </li>
      <li class="contact__item">
        <svg class="contact__icon" viewBox="0 0 10 10" aria-hidden="true"><circle cx="5" cy="5" r="4.5"/></svg>
        www.brenwickclinic.com
      </li>
    </ul>
  </section>
</body>
</html>
```